New CORPORATE WEBSITE DESIGN (Graphic layout for a WEBSITE TEMPLATE required - Photoshop files)

Hi – I need a draft created for a new corporate website for our company.
I need a graphic design concept which can be applied to a whole website layout -
I have a separate web development team who will implement the design onto Wordpress.
We are an Asian Buying Office based in Hong Kong and Shenzhen which facilitates relationships between factories in China and customers (retailers/etailers) all over the world.
We are a “boutique” agency, which offers highly customized services – we are highly consultative in our approach and tailor services to suit the needs of our customers with customized solutions. Our services are transparent partnership- and-integrity-based, and aimed to support at a certain size of company in growth mode.
We have dedicated teams of staff focused entirely on a customer’s business and we work TOGETHER with customers to solve their product design, patent, product engineering, goods production, quality control and supply chain challenges operating in 24/7 through our proprietary web-based supply chain platform called Cargoloom.
I have a PowerPoint which can be used to drive:
1) creative direction (colour palette etc) and to provide basic content for each “screen.” I would like to see design options based on the PowerPoint which offer creative ways to create a new look and feel for us for a corporate website which will not be social media enabled or ecommerce enabled. We do not put ANY customer brand names direct or references on our website – relationships are private. The home page of the website should say in the design style – “product design and branded global consumer goods” as well as “professional engineering and quality control proficiency”.
The website should be clean and functional – have the “usability” of the Vexor website but the “Calder 400” look & feel of the Oro & Tazz website (http://www.orotazz.com/eng/global/home.php) – Oro & Tazz is a benchmark for us. Oro & Tazz is the largest company in our industry doing what we do.
I do not want to COPY this example - I am offering it as a benchmark for a CLEAN, vibrant, professional site which sends a good brand and services message. The target market is a global B to B market – SMEs who are well funded and growing, brands with growth potential, or large, established brands who are looking to a) build a supply chain partner to help them grow b) increase their revenues by managing their costs c) reduce their risk through an experience buyer’s agent such as ourselves – a partner with integrity who they can trust. The web site design must say “global consumer brands” WITHOUT DIRECTLY ALLUDING TO THE LOGOS AND/OR BRAND NAMES WE WORK WITH , " full service agency – managing the process from product design and engineering, quality control and risk management to product manufacturing and shipping logistics" and “accountability/integrity/transparency within the partnership.” Designer to choose colors to be used in the design - I have also attached my logo file to allow you to select a color palette which will be complementary.
PLEASE FEEL FREE TO ASK ANY QUESTIONS - I AM HAPPY TO PROVIDE MORE DETAILS.
Described in the Project Description.
Graphic Design

```html
<!DOCTYPE html>
<html lang="en">
<head>
<meta charset="utf-8">
<title>Quillmere Industries Limited</title>
<link href="https://fonts.googleapis.com/css2?family=Arimo:wght@400;700&display=swap" rel="stylesheet">
<style>
  :root {
    --navy: #0b2d63;
    --navy-deep: #062250;
    --text-grey: #555555;
    --panel-grey: #ececec;
    --footer-grey: #7b7b7b;
    --white: #ffffff;
  }
  * { box-sizing: border-box; margin: 0; padding: 0; }
  html, body { width: 1200px; height: 762px; overflow: hidden; }
  body { font-family: "Arimo", Arial, sans-serif; background: var(--white); position: relative; }

  .hero-photo {
    position: absolute; left: 0; top: 0; width: 1200px; height: 420px;
    background:
      radial-gradient(ellipse 260px 320px at 860px 230px, #d9c6c0 0%, #b9a9b3 45%, rgba(120,150,200,0) 100%),
      linear-gradient(90deg, #8fb3de 0%, #b8d2ef 25%, #6f98cf 55%, #3f6db2 80%, #1d3f7c 100%);
  }

  .site-header {
    position: absolute; left: 120px; top: 0; width: 960px; height: 80px;
    background: linear-gradient(#ffffff, #f6f6f6);
    border-radius: 0 0 10px 10px;
  }
  .brand { position: absolute; left: 8px; top: 18px; display: flex; align-items: center; gap: 8px; }
  .brand-mark { width: 34px; height: 34px; border-radius: 50%; background: var(--navy); }
  .brand-text { color: var(--navy); font-weight: 700; }
  .brand-name { font-size: 17px; line-height: 20px; }
  .brand-tagline { font-size: 9px; font-weight: 400; color: var(--text-grey); text-align: right; }

  .search {
    position: absolute; left: 787px; top: 12px; width: 152px; height: 22px;
    border-radius: 11px; background: #f1f1f1; border: 1px solid #e2e2e2;
    font-size: 13px; color: #b5b5b5; padding: 3px 0 0 8px;
  }
  .search-button {
    position: absolute; right: -1px; top: -1px; width: 26px; height: 22px;
    border-radius: 11px; background: var(--navy);
  }
  .search-button svg { position: absolute; left: 6px; top: 4px; }

  .main-nav { position: absolute; right: 23px; top: 50px; display: flex; gap: 20px; }
  .main-nav a { color: var(--navy); font-size: 14px; font-weight: 700; text-decoration: none; }

  .hero-title { position: absolute; left: 172px; top: 132px; color: var(--white); }
  .hero-title .light { font-size: 46px; font-weight: 400; line-height: 48px; }
  .hero-title .bold { font-size: 36px; font-weight: 700; line-height: 36px; }
  .hero-copy {
    position: absolute; left: 171px; top: 219px; width: 423px; height: 94px;
    background: rgba(8, 42, 100, 0.85); color: var(--white);
    font-size: 12px; line-height: 14.5px; padding: 12px 14px;
  }
  .hero-dots { position: absolute; left: 566px; top: 377px; display: flex; gap: 2px; }
  .hero-dots span { width: 21px; height: 21px; border-radius: 50%; background: var(--white); }
  .hero-dots span.active { background: var(--navy); border: 3px solid var(--white); }

  .content-band {
    position: absolute; left: 0; top: 420px; width: 1200px; height: 310px;
    background: linear-gradient(#eeeeee 0px, #ffffff 55px);
  }
  .section-title {
    position: absolute; top: 22px; color: var(--navy);
    font-size: 18px; font-weight: 700; padding-bottom: 5px;
    border-bottom: 4px solid var(--navy);
  }
  .news-list { position: absolute; left: 120px; top: 60px; width: 449px; }
  .news-item {
    height: 49px; margin-bottom: 10px; background: var(--panel-grey);
    font-size: 12px; line-height: 14.5px; color: var(--text-grey); padding: 9px 6px;
  }
  .more { color: var(--navy); font-weight: 700; margin-left: 4px; }
  .scroll-track { position: absolute; left: 580px; top: 62px; width: 10px; height: 225px; border-radius: 5px; background: #eeeeee; }
  .scroll-thumb { width: 10px; height: 83px; border-radius: 5px; background: var(--navy); }

  .feature { position: absolute; top: 59px; width: 225px; }
  .feature-media {
    height: 149px; background: var(--panel-grey);
    display: flex; align-items: center; justify-content: center;
  }
  .logo-placeholder { font-size: 26px; font-weight: 700; color: #777777; }
  .video-brand { color: var(--navy); font-size: 17px; font-weight: 700; }
  .feature-heading { margin: 18px 0 0 -2px; font-size: 15px; font-weight: 700; color: var(--text-grey); }
  .feature-copy { margin-left: -2px; font-size: 12px; line-height: 14px; color: var(--text-grey); }

  .site-footer {
    position: absolute; left: 0; top: 730px; width: 1200px; height: 32px;
    background: var(--footer-grey); color: var(--white);
    font-size: 10px; text-align: center; padding-top: 10px;
  }
  .site-footer a { color: var(--white); margin-left: 4px; }
</style>
</head>
<body>
  <div class="hero-photo" role="img" aria-label="Glamour portrait of a woman wearing drop earrings against a blue bokeh background"></div>

  <header class="site-header">
    <div class="brand">
      <div class="brand-mark"></div>
      <div class="brand-text">
        <div class="brand-name">Quillmere Industries Limited</div>
        <div class="brand-tagline">Asian Sourcing Expertise</div>
      </div>
    </div>
    <div class="search">search
      <span class="search-button">
        <svg width="14" height="14" viewBox="0 0 14 14"><circle cx="5.5" cy="5.5" r="4" fill="none" stroke="#fff" stroke-width="2"/><line x1="8.5" y1="8.5" x2="12.5" y2="12.5" stroke="#fff" stroke-width="2.5" stroke-linecap="round"/></svg>
      </span>
    </div>
    <nav class="main-nav">
      <a href="#">Company</a><a href="#">Our Business</a><a href="#">Investor Relations</a><a href="#">News Releases</a><a href="#">Careers</a><a href="#">Contact Us</a>
    </nav>
  </header>

  <div class="hero-title">
    <div class="light">GLOBAL BRAND</div>
    <div class="bold">EQUITY ENHANCEMENT</div>
  </div>
  <p class="hero-copy">Lorem ipsum dolor sit amet, consectetur adipisicing elit, sed do eiusmod tempor incididunt ut labore et dolore magna aliqua. Ut enim ad minim veniam, quis nostrud exercitation ullamco laboris nisi ut aliquip ex ea commodo consequat. Duis aute irure dolor in reprehenderit in voluptate velit esse cillum dolore eu fugiat nulla pariatur.</p>
  <div class="hero-dots"><span class="active"></span><span></span><span></span></div>

  <main class="content-band">
    <h2 class="section-title" style="left:120px;width:470px;">What’s Happening</h2>
    <div class="news-list">
      <p class="news-item">Lorem ipsum dolor sit amet, consectetur adipisicing elit, sed do eiusmod tempor incididunt ut labore et dolore magna aliqua.<span class="more">[+]</span></p>
      <p class="news-item">Lorem ipsum dolor sit amet, consectetur adipisicing elit, sed do eiusmod tempor incididunt ut labore et dolore magna aliqua.<span class="more">[+]</span></p>
      <p class="news-item">Lorem ipsum dolor sit amet, consectetur adipisicing elit, sed do eiusmod tempor incididunt ut labore et dolore magna aliqua.<span class="more">[+]</span></p>
      <p class="news-item">Lorem ipsum dolor sit amet, consectetur adipisicing elit, sed do eiusmod tempor incididunt ut labore et dolore magna aliqua.<span class="more">[+]</span></p>
    </div>
    <div class="scroll-track"><div class="scroll-thumb"></div></div>

    <h2 class="section-title" style="left:610px;width:225px;">The Brands</h2>
    <section class="feature" style="left:610px;">
      <div class="feature-media"><span class="logo-placeholder">LOGO</span></div>
      <h3 class="feature-heading">Lorem ipsum dolor sit amet</h3>
      <p class="feature-copy">Lorem ipsum dolor sit amet, consectetur adipisicing elit, sed do eiusmod tempor incididunt ut labore et dolore magna <span class="more">[+]</span></p>
    </section>

    <h2 class="section-title" style="left:855px;width:225px;">Our Video</h2>
    <section class="feature" style="left:855px;">
      <div class="feature-media"><span class="video-brand">Quillmere Industries</span></div>
      <h3 class="feature-heading">Lorem ipsum dolor sit amet</h3>
      <p class="feature-copy">Lorem ipsum dolor sit amet, consectetur adipisicing elit, sed do eiusmod tempor incididunt ut labore et dolore magna <span class="more">[+]</span></p>
    </section>
  </main>

  <footer class="site-footer">© Copyright 2014 Quillmere Industries Limited. All rights reserved. <a href="#">Disclaimer and Privacy Statement</a></footer>
</body>
</html>
```